Need Amazing Website for Consulting Company

We need an amazing website design for a Human Resources Consulting Company. This will be geared towards a more professional crowd, but we don't want it to be overly corporate and stuffy: Just, clean and professional and amazing. Please use the video link below for further instruction.

http://clipvesta.net/v/kqPzRmN4

Thank You.

PS Logo file has been attached.

Target Market(s)

The target marketing is small business owners who have employees. These owners cant afford an in-house HR person so they would hire this client to consult and do the work for them.

Industry/Entity Type

It Company

Font styles to use
Sans Serif

Requirements
Must have
• Please watch video:

Must have spot for video on homepage.
Nice to have
• Clean, professional, but not overly corporate, we want a personal and fun feel to this site a bit to separate them from all the other executive type sites. This site should have some LIFE to it and reflect a local brand that is doing great things.
Should not have
• Should not be just a corporate site, should not be overly stuffy, should not be overly boring.

```html
<!DOCTYPE html>
<html lang="en">
<head>
<meta charset="utf-8">
<title>Mesa Ridge HR Consulting</title>
<link rel="stylesheet" href="https://fonts.googleapis.com/css2?family=Arimo:wght@400;700&family=Dosis:wght@500&family=Cormorant+SC:wght@700&family=Great+Vibes&display=swap">
<style>
:root{
  --red:#c8141b;
  --black:#000;
  --white:#fff;
  --ink:#111;
  --grey-tile:#555;
  --grey-card:#efefef;
  --grey-text:#555;
  --video-bg:#9a9a9a;
  --hero-dark:#3c2a1f;
  --hero-mid:#7a5a43;
  --nav-text:#555;
}
*{margin:0;padding:0;box-sizing:border-box}
html,body{width:1099px;height:1200px;overflow:hidden;background:var(--white)}
body{position:relative;font-family:'Arimo',Arial,sans-serif;color:var(--ink)}
.abs{position:absolute}

.site-header{position:absolute;left:0;top:0;width:1099px;height:62px;background:var(--white);box-shadow:0 2px 4px rgba(0,0,0,.35);z-index:2}
.brand{position:absolute;left:175px;top:14px;display:flex;align-items:center;gap:6px;font-family:'Arimo',sans-serif;font-weight:700;font-size:13px;line-height:15px;color:var(--ink);width:120px}
.brand-mark{width:10px;height:10px;background:var(--red);flex:none}
.main-nav a{position:absolute;top:0;height:62px;line-height:62px;font-family:'Dosis',sans-serif;font-weight:500;font-size:11px;letter-spacing:1.1px;color:var(--nav-text);text-decoration:none;text-transform:uppercase}
.main-nav a.is-active{background:var(--red);color:var(--white);text-align:center}

.hero{position:absolute;left:0;top:62px;width:1099px;height:380px;background:radial-gradient(ellipse at 50% 40%,var(--hero-mid) 0%,var(--hero-dark) 80%)}
.video-spot{position:absolute;left:171px;top:132px;width:414px;height:230px;background:var(--video-bg);box-shadow:4px 6px 14px rgba(0,0,0,.45)}
.video-name{position:absolute;left:0;width:414px;text-align:center;font-family:'Arimo',sans-serif;font-weight:700;color:var(--ink)}
.video-name.top{top:52px;font-size:21px}
.video-name.bottom{top:150px;font-size:16px}
.play-button{position:absolute;left:338px;top:215px}
.hero-intro{position:absolute;left:629px;top:166px;width:300px;font-size:15px;line-height:26px;color:var(--white)}

.tagline-band{position:absolute;left:0;top:442px;width:1099px;height:67px;background:var(--black);display:flex;align-items:center;justify-content:center;gap:12px;color:var(--white)}
.tagline-word{font-family:'Cormorant SC',serif;font-weight:700;font-size:38px}
.tagline-script{font-family:'Great Vibes',cursive;font-size:40px;color:var(--red)}

.service-title{position:absolute;top:571px;width:236px;text-align:center;font-size:20px;font-weight:400;color:var(--ink)}
.service-card{position:absolute;top:612px;width:236px;height:238px;background:var(--grey-card);box-shadow:4px 6px 5px rgba(0,0,0,.18)}
.service-card.is-featured{outline:3px solid var(--red);outline-offset:0}
.service-art{position:absolute;left:1px;top:1px;width:234px;height:166px;background:var(--grey-tile)}
.service-text{position:absolute;left:11px;top:179px;width:170px;font-size:11px;line-height:11px;color:var(--grey-text)}
.service-link{position:absolute;right:13px;top:216px;font-size:14px;color:var(--grey-text);text-decoration:underline}
.is-featured .service-link{color:var(--red)}

.site-footer{position:absolute;left:0;top:959px;width:1099px;height:217px;background:var(--black);color:var(--white)}
.contacts-heading{position:absolute;left:173px;top:17px;font-size:16px;font-weight:400;color:var(--red)}
.contacts-line{position:absolute;left:171px;font-size:9px;color:var(--white)}
.contacts-line .label{color:var(--red)}
.contacts-line .sep{margin:0 8px}
.social{position:absolute;top:38px;width:14px;height:14px;border-radius:50%;background:var(--white)}
.footer-rule{position:absolute;left:0;top:103px;width:1099px;height:1px;background:var(--red)}
.footer-nav{position:absolute;left:0;top:121px;width:1099px;text-align:center;font-size:11px}
.footer-nav a{color:var(--white);text-decoration:none}
.footer-nav a.is-active{color:var(--red)}
.footer-nav .sep{margin:0 8px}
.copyright{position:absolute;left:0;top:146px;width:1099px;text-align:center;font-size:9px;color:#9a9a9a}
.to-top{position:absolute;left:530px;top:1143px;width:50px;height:50px;background:var(--red);transform:rotate(45deg);z-index:3}
.to-top-arrow{position:absolute;left:557px;top:1148px;z-index:4}
</style>
</head>
<body>

<header class="site-header">
  <div class="brand"><span class="brand-mark"></span>Mesa Ridge HR</div>
  <nav class="main-nav">
    <a class="is-active" style="left:371px;width:58px">Home</a>
    <a style="left:443px">Recruitment</a>
    <a style="left:540px">Career Management</a>
    <a style="left:679px">HR Consulting</a>
    <a style="left:787px">Our Blog</a>
    <a style="left:865px">Contact Us</a>
  </nav>
</header>

<section class="hero" role="img" aria-label="Photograph of a chain of paper cut-out people holding hands on a wooden table"></section>
<div class="video-spot" role="img" aria-label="Introductory video">
  <div class="video-name top">MESA RIDGE HR</div>
  <div class="video-name bottom">Consulting, LLC</div>
</div>
<svg class="abs play-button" width="74" height="56" viewBox="0 0 74 56" aria-hidden="true">
  <circle cx="37" cy="28" r="26" fill="#1a1a1a" opacity=".8"/>
  <path d="M30 16 L50 28 L30 40 Z" fill="#fff"/>
</svg>
<p class="hero-intro">Mesa Ridge HR Consulting, LLC<br>is an experienced consulting agency<br>that is committed to providing businesses<br>with effective and efficient Human Resources<br>support by developing partnerships to meet<br>company’s individual needs.</p>

<div class="tagline-band">
  <span class="tagline-word">Effective.</span>
  <span class="tagline-script">Experienced.</span>
  <span class="tagline-word">Efficient.</span>
</div>

<h2 class="service-title" style="left:165px">Recruitment</h2>
<h2 class="service-title" style="left:433px">Career Management</h2>
<h2 class="service-title" style="left:689px">HR Consulting</h2>

<article class="service-card" style="left:170px">
  <div class="service-art">
    <svg width="234" height="166" viewBox="0 0 234 166" aria-hidden="true">
      <circle cx="90" cy="64" r="43" fill="none" stroke="#fff" stroke-width="4"/>
      <path d="M121 95 L132 98 L192 137 L185 146 L128 106 Z" fill="#fff"/>
    </svg>
  </div>
  <p class="service-text">Lorem ipsum dolor sit amet, con-<br>sectetur adipiscing elit.</p>
  <a class="service-link">Learn more</a>
</article>

<article class="service-card is-featured" style="left:431px">
  <div class="service-art">
    <svg width="234" height="166" viewBox="0 0 234 166" aria-hidden="true">
      <rect x="91" y="24" width="84" height="102" fill="#555" stroke="#fff" stroke-width="4"/>
      <rect x="145" y="34" width="17" height="15" fill="#fff"/>
      <path d="M103 42h32M110 60h53M110 74h53M110 88h53M110 102h53" stroke="#fff" stroke-width="4"/>
      <rect x="51" y="54" width="76" height="85" fill="#555" stroke="#fff" stroke-width="4"/>
      <rect x="102" y="64" width="16" height="14" fill="#fff"/>
      <path d="M61 72h32M61 87h57M61 101h57M61 115h57" stroke="#fff" stroke-width="4"/>
    </svg>
  </div>
  <p class="service-text">Lorem ipsum dolor sit amet, con-<br>sectetur adipiscing elit.</p>
  <a class="service-link">Learn more</a>
</article>

<article class="service-card" style="left:691px">
  <div class="service-art">
    <svg width="234" height="166" viewBox="0 0 234 166" aria-hidden="true">
      <circle cx="67" cy="53" r="16" fill="#fff"/>
      <circle cx="172" cy="53" r="16" fill="#fff"/>
      <path d="M54 75 H80 V137 H50 Q43 137 43 130 V85 Q43 75 54 75 Z" fill="none" stroke="#fff" stroke-width="4"/>
      <path d="M185 75 H159 V137 H189 Q196 137 196 130 V85 Q196 75 185 75 Z" fill="none" stroke="#fff" stroke-width="4"/>
      <circle cx="120" cy="47" r="19" fill="#555"/>
      <circle cx="120" cy="47" r="18" fill="#fff"/>
      <path d="M100 73 H140 Q150 73 150 83 V140 Q150 148 142 148 H98 Q90 148 90 140 V83 Q90 73 100 73 Z" fill="#555" stroke="#fff" stroke-width="4"/>
      <path d="M116 75 H124 L126 92 L120 100 L114 92 Z" fill="#fff"/>
    </svg>
  </div>
  <p class="service-text">Lorem ipsum dolor sit amet, con-<br>sectetur adipiscing elit.</p>
  <a class="service-link">Learn more</a>
</article>

<footer class="site-footer">
  <h3 class="contacts-heading">Contacts</h3>
  <p class="contacts-line" style="top:39px">Mesa Ridge HR Consulting, LLC<span class="sep">::</span>Juniper Lane 12, Santa Fe, NM</p>
  <p class="contacts-line" style="top:56px"><span class="label">Phone:</span> +1 505-555-0142<span class="sep">::</span><span class="label">E-mail:</span> hello@mesaridgehr.com</p>
  <span class="social" style="left:816px" role="img" aria-label="Social network link"></span>
  <span class="social" style="left:847px" role="img" aria-label="Social network link"></span>
  <span class="social" style="left:880px" role="img" aria-label="Social network link"></span>
  <span class="social" style="left:911px" role="img" aria-label="Social network link"></span>
  <div class="footer-rule"></div>
  <nav class="footer-nav">
    <a class="is-active">Home</a><span class="sep">::</span><a>Recruitment</a><span class="sep">::</span><a>Career Management</a><span class="sep">::</span><a>HR Consulting</a><span class="sep">::</span><a>Our Blog</a><span class="sep">::</span><a>Contact Us</a>
  </nav>
  <p class="copyright">Copyright MRHRC. All Right Reserved.</p>
</footer>
<div class="to-top"></div>
<svg class="abs to-top-arrow" width="10" height="10" viewBox="0 0 10 10" aria-hidden="true">
  <path d="M5 1 L9 5 H6 V9 H4 V5 H1 Z" fill="#fff"/>
</svg>

</body>
</html>
```